Lomtra - 'Destination Metasearch'

We want to make travel research and booking simple and easy within one product by enabling our users to compare destinations.

As such, we are looking for web designers to create mockups of what this ‘destination comparison’ search page could look like. Where possible, we would like for the site to remain using lomtra colours (www.lomtra-example.com).

Attached is a design brief that includes:

1) Company profile
- General information about us
- Audience and markets

2) Project overview
- Problem statement
- What is the project
- Expected deliverables
- Key functionalities
- User flow

An example mockup has been attached.

Designs should be mobile-first

Industry/Entity Type

Travel

Number of Pages Required

1 page

Requirements
Must have
• It must compare a destination using data for both travel and accommodation (see mockup example) and MUST be a mobile design
Nice to have
• Inclusion of additional data points (i.e. weather)
Should not have
• It must not only consider one aspect (i.e. hotel / transport).

```html
<!DOCTYPE html>
<html lang="en">
<head>
<meta charset="utf-8">
<title>Lomtra – Destination Metasearch</title>
<link rel="stylesheet" href="https://fonts.googleapis.com/css2?family=Montserrat:wght@800&family=Roboto:ital,wght@0,400;0,500;0,700;1,400&display=swap">
<style>
:root{
  --stage:#5e5e5e;
  --screen:#ebeaf4;
  --teal:#10999f;
  --navy:#333a78;
  --label:#8a8fb0;
  --pill-dark:#363845;
  --book:#5b5b5e;
  --white:#ffffff;
  --rule:#cfd1dd;
  --grid:#b9bccb;
}
*{box-sizing:border-box;margin:0;padding:0}
html,body{width:1200px;height:768px;overflow:hidden}
body{background:var(--stage);font-family:"Roboto",Arial,sans-serif;position:relative;color:var(--navy)}
.screen{position:absolute;top:36px;width:318px;height:698px;background:var(--screen);border-radius:26px;overflow:hidden}
.screen--start{left:81px}
.screen--results{left:453px}
.screen--details{left:816px}
.hero{height:133px;background:
  radial-gradient(ellipse 60px 30px at 25% 85%,#d8336f 0%,rgba(216,51,111,0) 100%),
  radial-gradient(ellipse 70px 28px at 70% 95%,#c82c6a 0%,rgba(200,44,106,0) 100%),
  radial-gradient(ellipse 80px 40px at 45% 35%,#3f7a35 0%,rgba(63,122,53,0) 100%),
  radial-gradient(ellipse 70px 50px at 90% 40%,#4d8c3a 0%,rgba(77,140,58,0) 100%),
  linear-gradient(160deg,#c9b48a 0%,#d9c59d 30%,#5bb6ad 55%,#2f9ca3 100%)}
.headline{text-align:center;margin-top:15px}
.headline h1{font-family:"Montserrat",Arial,sans-serif;font-weight:800;font-size:11.5px;color:var(--teal);letter-spacing:.1px}
.headline p{font-size:4.3px;color:#3b3d52;margin-top:4px;font-weight:500}
.search-card{position:absolute;top:184px;left:12px;width:289px;height:106px;background:var(--white);border-radius:8px;box-shadow:2px 3px 4px rgba(0,0,0,.25);padding:10px 13px}
.trip-tabs{display:flex;gap:3px}
.trip-tabs span{width:31px;height:14px;border:1px solid #d7d8e4;border-radius:8px;font-size:3.4px;display:flex;align-items:center;justify-content:center;color:var(--label)}
.trip-tabs .is-active{background:var(--pill-dark);border-color:var(--pill-dark);color:var(--white);font-weight:700}
.field{position:absolute;width:48px}
.field .label{font-size:3.8px;color:var(--label);font-weight:500}
.field .value{font-size:6.2px;font-weight:500;color:var(--navy);margin-top:5px;height:10px;border-bottom:1px solid var(--rule)}
.swap-dot{position:absolute;left:67px;top:41px;width:10px;height:10px;border-radius:50%;background:#d8d9e6}
.chevron{position:absolute;right:2px;top:2px}
.search-btn{position:absolute;left:156px;top:75px;width:120px;height:19px;background:var(--teal);border-radius:10px;color:var(--white);font-size:5px;font-weight:500;display:flex;align-items:center;justify-content:center;gap:4px}
.compare-row{position:absolute;left:25px;width:270px;display:flex;justify-content:space-between}
.compare-box{width:125px;height:42px;background:var(--teal);box-shadow:2px 2px 3px rgba(0,0,0,.35);padding:3px 3px 0 3px}
.compare-box h2{font-size:7.4px;font-weight:500;color:var(--white)}
.compare-box .inputs{display:flex;gap:3px;margin-top:3px;padding-left:1px}
.compare-box .input{width:74px;height:11px;background:var(--white)}
.compare-box .go{width:40px;height:11px;background:var(--white);font-size:7.2px;font-weight:500;color:var(--navy);display:flex;align-items:center;justify-content:center}
.compare-box .hint{font-size:7px;font-style:italic;color:var(--white);margin-top:2px;padding-left:2px}
.dest-card{width:119px;background:var(--white);border-radius:6px;box-shadow:1px 2px 3px rgba(0,0,0,.3);padding:5px}
.dest-photo{height:81px;border-radius:5px}
.photo-temple{background:linear-gradient(180deg,#3e8fd6 0%,#a9cde8 45%,#4a5a48 70%,#3c6c9e 100%)}
.photo-bungalow{background:linear-gradient(180deg,#3a8fd8 0%,#bfe0ef 35%,#9a8b66 52%,#37cdd0 65%,#23c0c6 100%)}
.dest-meta{display:flex;justify-content:space-between;align-items:center;padding:7px 0 4px 2px}
.dest-meta h3{font-size:6px;font-weight:700;color:var(--navy)}
.dest-meta small{display:block;font-size:3.8px;color:var(--label);margin-top:2px}
.book{width:39px;height:12px;border-radius:7px;background:var(--book);color:var(--white);font-size:3.6px;font-weight:700;display:flex;align-items:center;justify-content:center}
.compare-table{width:100%;border-collapse:collapse;margin-top:3px;font-size:2.6px;line-height:1.15;color:#333}
.compare-table td{border:0.5px solid var(--grid);padding:1.5px 2px;vertical-align:top}
.compare-table .group{color:var(--teal);font-weight:700;font-size:3px;width:38px}
.compare-table .val{width:18px}
.dest-card--long{height:250px}
</style>
</head>
<body>

<!-- Screen 1: empty comparison -->
<section class="screen screen--start">
  <div class="hero" role="img" aria-label="Tropical beach photo seen through pink flowers and palm leaves"></div>
  <div class="headline"><h1>COMPARE YOUR DESTINATION</h1><p>Book Domestic and International flights</p></div>
  <div class="search-card">
    <div class="trip-tabs"><span>One Way</span><span class="is-active">Round Trip</span><span>Multi City</span></div>
    <div class="field" style="left:13px;top:36px"><div class="label">FROM</div><div class="value">New York (NYC)</div></div>
    <div class="swap-dot"></div>
    <div class="field" style="left:85px;top:36px"><div class="label">TO</div><div class="value"></div></div>
    <div class="field" style="left:156px;top:36px"><div class="label">DEPARTURE</div><div class="value">Monday, 18 Mar</div></div>
    <div class="field" style="left:228px;top:36px"><div class="label">RETURN</div><div class="value">Sunday, 24 Mar</div></div>
    <div class="field" style="left:13px;top:75px"><div class="label">PASSENGERS</div><div class="value">3</div></div>
    <div class="field" style="left:85px;top:75px"><div class="label">CLASS</div><div class="value">Business</div>
      <svg class="chevron" style="top:12px" width="6" height="4" viewBox="0 0 6 4"><path d="M.5.5 3 3 5.5.5" fill="none" stroke="#8a8fb0" stroke-width=".7"/></svg></div>
    <div class="search-btn">Search Flights <svg width="8" height="8" viewBox="0 0 10 10"><path d="M1 5h8M6 2l3 3-3 3M4 2.5 5.5 5 4 7.5" fill="none" stroke="#fff" stroke-width="1.2"/></svg></div>
  </div>
  <div class="compare-row" style="top:302px">
    <div class="compare-box"><h2>COMPARE WITH</h2><div class="inputs"><div class="input"></div><div class="go">SEARCH</div></div><p class="hint">please enter destination</p></div>
    <div class="compare-box"><h2>COMPARE WITH</h2><div class="inputs"><div class="input"></div><div class="go">SEARCH</div></div><p class="hint">please enter destination</p></div>
  </div>
</section>

<!-- Screen 2: destination results -->
<section class="screen screen--results">
  <div class="hero" role="img" aria-label="Tropical beach photo seen through pink flowers and palm leaves"></div>
  <div class="headline"><h1>COMPARE YOUR DESTINATION</h1><p>Book Domestic and International flights</p></div>
  <div class="search-card">
    <div class="trip-tabs"><span>One Way</span><span class="is-active">Round Trip</span><span>Multi City</span></div>
    <div class="field" style="left:13px;top:36px"><div class="label">FROM</div><div class="value">New York (NYC)</div></div>
    <div class="swap-dot"></div>
    <div class="field" style="left:85px;top:36px"><div class="label">TO</div><div class="value"></div></div>
    <div class="field" style="left:156px;top:36px"><div class="label">DEPARTURE</div><div class="value">Monday, 18 Mar</div></div>
    <div class="field" style="left:228px;top:36px"><div class="label">RETURN</div><div class="value">Sunday, 24 Mar</div></div>
    <div class="field" style="left:13px;top:75px"><div class="label">PASSENGERS</div><div class="value">3</div></div>
    <div class="field" style="left:85px;top:75px"><div class="label">CLASS</div><div class="value">Business</div>
      <svg class="chevron" style="top:12px" width="6" height="4" viewBox="0 0 6 4"><path d="M.5.5 3 3 5.5.5" fill="none" stroke="#8a8fb0" stroke-width=".7"/></svg></div>
    <div class="search-btn">Search Flights <svg width="8" height="8" viewBox="0 0 10 10"><path d="M1 5h8M6 2l3 3-3 3M4 2.5 5.5 5 4 7.5" fill="none" stroke="#fff" stroke-width="1.2"/></svg></div>
  </div>
  <div class="compare-row" style="top:306px">
    <div class="compare-box"><h2>COMPARE WITH</h2><div class="inputs"><div class="input"></div><div class="go">SEARCH</div></div><p class="hint">please enter destination</p></div>
    <div class="compare-box"><h2>COMPARE WITH</h2><div class="inputs"><div class="input"></div><div class="go">SEARCH</div></div><p class="hint">please enter destination</p></div>
  </div>
  <div class="compare-row" style="top:352px">
    <article class="dest-card"><div class="dest-photo photo-temple" role="img" aria-label="Lakeside temple with tiered roofs under a blue sky"></div>
      <div class="dest-meta"><div><h3>Grand Canyon, USA</h3><small>FROM&nbsp; $2320</small></div><div class="book">BOOK</div></div></article>
    <article class="dest-card"><div class="dest-photo photo-bungalow" role="img" aria-label="Thatched overwater bungalows over turquoise sea"></div>
      <div class="dest-meta"><div><h3>Lake District, USA</h3><small>FROM&nbsp; $2620</small></div><div class="book">BOOK</div></div></article>
  </div>
</section>

<!-- Screen 3: detailed comparison -->
<section class="screen screen--details">
  <div class="hero" role="img" aria-label="Tropical beach photo seen through pink flowers and palm leaves"></div>
  <div class="headline"><h1>COMPARE YOUR DESTINATION</h1><p>Book Domestic and International flights</p></div>
  <div class="search-card">
    <div class="trip-tabs"><span>One Way</span><span class="is-active">Round Trip</span><span>Multi City</span></div>
    <div class="field" style="left:13px;top:36px"><div class="label">FROM</div><div class="value">New York (NYC)</div></div>
    <div class="swap-dot"></div>
    <div class="field" style="left:85px;top:36px"><div class="label">TO</div><div class="value"></div></div>
    <div class="field" style="left:156px;top:36px"><div class="label">DEPARTURE</div><div class="value">Monday, 18 Mar</div></div>
    <div class="field" style="left:228px;top:36px"><div class="label">RETURN</div><div class="value">Sunday, 24 Mar</div></div>
    <div class="field" style="left:13px;top:75px"><div class="label">PASSENGERS</div><div class="value">3</div></div>
    <div class="field" style="left:85px;top:75px"><div class="label">CLASS</div><div class="value">Business</div>
      <svg class="chevron" style="top:12px" width="6" height="4" viewBox="0 0 6 4"><path d="M.5.5 3 3 5.5.5" fill="none" stroke="#8a8fb0" stroke-width=".7"/></svg></div>
    <div class="search-btn">Search Flights <svg width="8" height="8" viewBox="0 0 10 10"><path d="M1 5h8M6 2l3 3-3 3M4 2.5 5.5 5 4 7.5" fill="none" stroke="#fff" stroke-width="1.2"/></svg></div>
  </div>
  <div class="compare-row" style="top:305px">
    <div class="compare-box"><h2>COMPARE WITH</h2><div class="inputs"><div class="input"></div><div class="go">SEARCH</div></div><p class="hint">please enter destination</p></div>
    <div class="compare-box"><h2>COMPARE WITH</h2><div class="inputs"><div class="input"></div><div class="go">SEARCH</div></div><p class="hint">please enter destination</p></div>
  </div>
  <div class="compare-row" style="top:350px">
    <article class="dest-card dest-card--long"><div class="dest-photo photo-temple" role="img" aria-label="Lakeside temple with tiered roofs under a blue sky"></div>
      <div class="dest-meta"><div><h3>Grand Canyon, USA</h3><small>FROM&nbsp; $2320</small></div><div class="book">BOOK</div></div>
      <table class="compare-table">
        <tr><td class="group" rowspan="4">ACCOMMODATION</td><td>Min. price<br>(optional) Avg. price</td><td class="val">xxxxxx</td></tr>
        <tr><td>Distance from accommodation to city center (up to 5km as default)/rating</td><td class="val">xxxxxxx</td></tr>
        <tr><td>Type (hotel or apartment)</td><td class="val">xxxxxxx</td></tr>
        <tr><td>(optional) outline two offers, hotel / apartment</td><td class="val">xxxxxxxx</td></tr>
        <tr><td class="group" rowspan="6">TRANSPORTATION</td><td>Departure time</td><td class="val">xxxxxxxx</td></tr>
        <tr><td>Arrival time</td><td class="val">xxxxxxxx</td></tr>
        <tr><td>Duration<br>(from arrival city to destination)</td><td class="val">xxxxxxxx</td></tr>
        <tr><td>Transport type (bus, train, plane). You may show one option per transport type</td><td class="val">xxxxxxx</td></tr>
        <tr><td>Min. price</td><td class="val">xxxxxxx</td></tr>
        <tr><td>Number of changes</td><td class="val">xxxxxx</td></tr>
        <tr><td class="group">TOTAL PRICE<br>(ACCOMMODATION + TRANSPORT)</td><td></td><td class="val">xxxxxxx</td></tr>
      </table></article>
    <article class="dest-card dest-card--long"><div class="dest-photo photo-bungalow" role="img" aria-label="Thatched overwater bungalows over turquoise sea"></div>
      <div class="dest-meta"><div><h3>Lake District, USA</h3><small>FROM&nbsp; $2620</small></div><div class="book">BOOK</div></div>
      <table class="compare-table">
        <tr><td class="group" rowspan="4">ACCOMMODATION</td><td>Min. price<br>(optional) Avg. price</td><td class="val">xxxxxx</td></tr>
        <tr><td>Distance from accommodation to city center (up to 5km as default)/rating</td><td class="val">xxxxxxx</td></tr>
        <tr><td>Type (hotel or apartment)</td><td class="val">xxxxxxx</td></tr>
        <tr><td>(optional) outline two offers, hotel / apartment</td><td class="val">xxxxxxxx</td></tr>
        <tr><td class="group" rowspan="6">TRANSPORTATION</td><td>Departure time</td><td class="val">xxxxxxxx</td></tr>
        <tr><td>Arrival time</td><td class="val">xxxxxxxx</td></tr>
        <tr><td>Duration<br>(from arrival city to destination)</td><td class="val">xxxxxxxx</td></tr>
        <tr><td>Transport type (bus, train, plane). You may show one option per transport type</td><td class="val">xxxxxxx</td></tr>
        <tr><td>Min. price</td><td class="val">xxxxxxx</td></tr>
        <tr><td>Number of changes</td><td class="val">xxxxxx</td></tr>
        <tr><td class="group">TOTAL PRICE<br>(ACCOMMODATION + TRANSPORT)</td><td></td><td class="val">xxxxxxx</td></tr>
      </table></article>
  </div>
</section>

</body>
</html>
```